依頼詳細
《チラシのイメージ》
複数の写真やイラストの使用は避けてください。子育て世代向けへの広告とは一線画した差別化されたデザインを希望しています。また、子どもにフォーカスするのではなく、子育てママをフォーカスしていると一目でわかるビジュアルに仕上げてください。

※前回は塗り絵を前面に押しましたが、今回はその必要はありません。
(前回のチラシは添付データーをご参照ください)
理由は、前回は塗り絵に興味がある人への告知になってましたが、今回は子育てする親がセミナーに参加したくなるものにしてください。
《ターゲット》
お子さんの年齢は6歳以下の未就学児がいる中間層の子育て家族。

《デザインへの希望》
フォントのデザイン・文字サイズにメリハリをつけてください。
広告を見た瞬間に詳しく読みたくなるキャッチをメインにして「いつ開催?」「どこで開催?」は分かり易く見易く、その後、詳しく読みたくなる部分や、参加希望する人が必ず確認する部分については、小さな文字にしていただくことで、デザイン構成ください。

参加費無料や定員など、営業に映るような部分も、当会は堺貢献事業として活動している団体のため、営業的に映る部分については大きく目立つ表記は避けてください。さりげなく表記いただき、見れば分かる記述で結構です。

いろんな色を使用することで、ゴチャゴチャして大切な部分が見えなくなってしまうのは避けてください。

《セミナー構成》
前半:親への子育てセミナー
後半:子ども塗り絵診断

【キャッチ】
▮子どもと「ちょうどいい」距離感
または
▮子どもの世界をつくる
ママのひとり時間をつくる

【サブキャッチ】
▮子どもが言葉を話すようになったら...それは自分の世界を広げたいサイン

【リード文】
▮子育ての順番は「手を掛ける」「目を掛ける」「気を掛ける」どのタイミングでステップアップするかは、それぞれの子どもによって違う。子育てについて「周りは?」ついそう思ってしまいがち。周りを気にするのは誰かと比較してること。もっと色んな視点から子どもを見つめてみると見えてくるもの。早くから子どもの世界づくりをはじめ、親も自分時間を持つことで親子のちょうどいい距離感が生まれる。

【セミナー内容】
Lesson1ママパパ学び
・子どもの世界
・子どもの世界を広げるタイミング
・ヤル気のONスイッチ
・ちょうどいい子どもとの距離感
・子どもが成長してしまう3つのアプロ―チ
・子育て計画「コト・モノ・オカネ」

Lesson2子ども学び
・個性を見つける10の視点
・塗り絵診断
・子どもは天才の卵!
・生まれもった性格

【詳細】
テーマ:はじめての習いごと
開催日:8月24日(土)
時間:14時~16時
参加費:無料
定員:8家族(夫婦・親子でご参加ください)
開催場所:北嶺市民活動センター「ひだまる」
(兵庫県緑沢市緑野町桜台字松ノ木45-3)
対象者:子ども年齢/1歳2か月~6歳
(参加にはお申込みが必要です)
主催:そらいるか(一般社団法人家庭育成推進協会)
後援:緑沢市 緑沢市教育委員会
講師:そらいるか認定講師
受付:そらいるか事務局
〒541-0093大阪市中央区東浜町3-2-5-208
TEL0120-870-041
06-6912-4537    ※電話受付は平日9時~17時のみ
(メールは不要)

ホームページからのお申込みは▼
QRコード

記載項目
主催:そらいるか(一般社団法人家庭育成推進協会)
〒541-0093 大阪府大阪市中央区東浜町3-2-5-208
TEL:06-6912-4537 FAX:06-6912-4538
サイズ
A4
ページ数
片面
希望イメージ
シンプル 複雑
単色 カラフル
暗い 明るい
日常 高級
遊び心 厳粛
未来的 伝統的
女性的 男性的
希望する色
黄・オレンジ系
納品ファイル
• イラストレーター形式 (.ai)
補足説明
今回のセミナーは、過去に何度も開催しており、少しづつブラッシュアップしていってます。ワークポッドを利用するのは今回で2回目です。前回は21,600円でコンペに出しましたが、今回は要望内容が多いため54,000円でコンペに応募します。
現在、緑沢市と緑沢市教育委員会に後援申請をしています。後援の許可の有無により、後援名の部分の修正をお願いする可能性があります。またご提案いただいたチラシ内容は、法人の理事長の許可を必要としますので何度か修正をお願いすると思います。ご質問等がありましたら、ご連絡ください。

スッキリとまとまっており、一番目に飛び込んでくる構成になっているところが良かったです。
また、修正する場合に作業がしやすいデザインになっていると思えたところが良かったです。

沢山提案していただきありがとうございました。
また、こちらの都合で決めるのに時間がかかり申し訳ありませんでした。

```html
<!DOCTYPE html>
<html lang="ja">
<head>
<meta charset="utf-8">
<title>はじめての習いごと セミナー</title>
<link rel="stylesheet" href="https://fonts.googleapis.com/css2?family=M+PLUS+Rounded+1c:wght@500;700;800&family=Noto+Sans+JP:wght@400;500;700;900&display=swap">
<style>
:root{
  --orange:#e8822a;
  --orange-deep:#d9661c;
  --yellow:#f6b93b;
  --cream:#fff9ee;
  --brown:#5a3a22;
  --text:#3d2a1c;
  --line:#f0b468;
  --white:#ffffff;
}
*{box-sizing:border-box;margin:0;padding:0}
html,body{width:849px;height:1200px;overflow:hidden;background:var(--white)}
body{font-family:"Noto Sans JP",sans-serif;color:var(--text)}
.flyer{position:relative;width:849px;height:1200px;background:var(--cream);overflow:hidden}

.event-box{position:absolute;left:22px;top:22px;width:530px;height:300px;border:3px solid var(--yellow);border-radius:6px;background:var(--white)}
.badge{position:absolute;left:100px;top:0;width:180px;height:44px;background:var(--orange);color:var(--white);font:700 24px "M PLUS Rounded 1c",sans-serif;text-align:center;line-height:44px;border-radius:0 0 8px 8px}
.title{position:absolute;left:0;width:100%;top:60px;text-align:center;font:800 46px "M PLUS Rounded 1c",sans-serif;color:var(--brown);letter-spacing:2px}
.date{position:absolute;left:24px;top:150px;font:900 92px/1 "Noto Sans JP",sans-serif;color:var(--orange-deep);letter-spacing:-2px}
.date .dow{display:inline-block;width:52px;height:52px;border-radius:50%;background:var(--orange-deep);color:var(--white);font-size:32px;line-height:52px;text-align:center;vertical-align:middle;margin-left:6px;letter-spacing:0}
.time{position:absolute;left:340px;top:170px;font:700 34px/1.25 "Noto Sans JP",sans-serif;color:var(--brown)}
.lecturer{position:absolute;right:14px;top:272px;font-size:15px;color:var(--brown)}

.info{position:absolute;left:28px;top:332px;width:400px;font-size:14px;line-height:1.35;border-collapse:collapse}
.info th{width:84px;background:var(--orange);color:var(--white);font-weight:700;padding:5px 4px;border-bottom:3px solid var(--cream);text-align:center;vertical-align:middle}
.info td{padding:5px 8px;border-bottom:1px dashed var(--line);font-weight:500}
.info .venue{font-size:18px;font-weight:900;color:var(--brown)}
.info .note{font-size:11px}

.tag{position:absolute;left:610px;top:14px;width:222px;height:48px;background:var(--orange);color:var(--white);font:700 23px/48px "M PLUS Rounded 1c",sans-serif;text-align:center}
.catch{position:absolute;writing-mode:vertical-rl;font:900 68px/1 "Noto Sans JP",sans-serif}
.catch-main{left:740px;top:78px;color:var(--orange-deep)}
.catch-main em{font-style:normal;color:var(--brown)}
.catch-end{left:660px;top:74px;color:var(--brown)}

.lesson1{position:absolute;left:440px;top:420px;width:270px;height:350px}
.lesson1 .label{position:absolute;left:60px;top:0;width:150px;height:40px;background:var(--orange);border-radius:20px;color:var(--white);font:700 22px/40px "M PLUS Rounded 1c",sans-serif;text-align:center}
.lesson-card{position:absolute;background:var(--white);border:3px solid var(--orange);border-radius:18px;padding:36px 14px 14px}
.lesson1 .lesson-card{left:0;top:20px;width:270px;height:330px}
.lesson-card h3{font:800 22px "M PLUS Rounded 1c",sans-serif;color:var(--orange-deep);margin-bottom:8px;text-align:center}
.lesson-card li{list-style:none;font-size:14px;line-height:1.55;font-weight:500}
.lesson-card li::before{content:"・";color:var(--orange)}

.lesson2{position:absolute;left:28px;top:560px;width:250px;height:220px}
.lesson2 .label{position:absolute;left:60px;top:0;width:130px;height:36px;background:var(--orange);border-radius:18px;color:var(--white);font:700 19px/36px "M PLUS Rounded 1c",sans-serif;text-align:center;z-index:1}
.lesson2 .lesson-card{left:0;top:18px;width:250px;height:202px;padding-top:30px}

.subcatch{position:absolute;left:40px;width:680px;top:800px;text-align:center;font:700 27px/1.45 "M PLUS Rounded 1c",sans-serif;color:var(--brown)}
.subcatch strong{color:var(--orange-deep)}
.lead{position:absolute;left:70px;width:710px;top:900px;font-size:13px;line-height:1.7;text-align:justify}

.footer{position:absolute;left:0;top:1005px;width:849px;height:195px;background:var(--white);border-top:4px solid var(--yellow)}
.org{position:absolute;left:40px;top:20px;font-size:16px;line-height:1.7}
.org .mark{display:inline-block;width:30px;height:30px;border-radius:50%;background:var(--yellow);vertical-align:middle;margin-right:8px}
.org b{font-weight:700;color:var(--brown)}
.phone{position:absolute;left:110px;top:92px;font:900 40px/1 "Noto Sans JP",sans-serif;color:var(--orange-deep)}
.phone svg{vertical-align:-4px;margin-right:6px}
.tel-sub{position:absolute;left:150px;top:146px;font-size:13px}
.square{position:absolute;left:20px;top:100px;width:72px;height:72px;background:var(--line);border-radius:4px}
.office{position:absolute;right:26px;top:100px;text-align:right;font-size:12px;line-height:1.5}
.office b{display:block;font:700 22px "M PLUS Rounded 1c",sans-serif;color:var(--brown)}
</style>
</head>
<body>
<main class="flyer">
  <section class="event-box">
    <div class="badge">セミナー</div>
    <h1 class="title">はじめての習いごと</h1>
    <p class="date">8/24<span class="dow">土</span></p>
    <p class="time">14:00〜<br>16:00</p>
    <p class="lecturer">講師：そらいるか認定講師</p>
  </section>

  <table class="info">
    <tr><th>開催場所</th><td><span class="venue">北嶺市民活動センター「ひだまる」</span><br><span class="note">（兵庫県緑沢市緑野町桜台字松ノ木45-3）</span></td></tr>
    <tr><th>参加費</th><td>無料</td></tr>
    <tr><th>定　員</th><td>8家族（夫婦・親子でご参加ください）</td></tr>
    <tr><th>対象者</th><td>子ども年齢／1歳2か月〜6歳<br><span class="note">（参加にはお申込みが必要です）</span></td></tr>
  </table>

  <div class="tag">子育て「学び場」</div>
  <h2 class="catch catch-main">子どもと<em>「ちょうどいい」</em></h2>
  <p class="catch catch-end">距離感。</p>

  <section class="lesson1">
    <div class="lesson-card">
      <h3>ママパパ学び</h3>
      <ul>
        <li>子どもの世界</li>
        <li>子どもの世界を広げるタイミング</li>
        <li>ヤル気のONスイッチ</li>
        <li>ちょうどいい子どもとの距離感</li>
        <li>子どもが成長してしまう3つのアプローチ</li>
        <li>子育て計画「コト・モノ・オカネ」</li>
      </ul>
    </div>
    <div class="label">Lesson 1</div>
  </section>

  <section class="lesson2">
    <div class="label">Lesson 2</div>
    <div class="lesson-card">
      <h3>子ども学び</h3>
      <ul>
        <li>個性を見つける10の視点</li>
        <li>塗り絵診断</li>
        <li>子どもは天才の卵！</li>
        <li>生まれもった性格</li>
      </ul>
    </div>
  </section>

  <p class="subcatch">子どもが<strong>言葉</strong>を話すようになったら…<br>それは自分の世界を広げたいサイン</p>
  <p class="lead">子育ての順番は「手を掛ける」「目を掛ける」「気を掛ける」。どのタイミングでステップアップするかは、それぞれの子どもによって違う。子育てについて「周りは？」ついそう思ってしまいがち。周りを気にするのは誰かと比較していること。もっと色んな視点から子どもを見つめてみると見えてくるもの。早くから子どもの世界づくりをはじめ、親も自分時間を持つことで親子のちょうどいい距離感が生まれる。</p>

  <footer class="footer">
    <p class="org"><span class="mark"></span>主催：<b>そらいるか</b>（一般社団法人家庭育成推進協会）<br>後援：緑沢市　緑沢市教育委員会</p>
    <div class="square" role="img" aria-label="申込み用の案内マーク"></div>
    <p class="phone"><svg width="34" height="34" viewBox="0 0 24 24"><path fill="currentColor" d="M6.6 10.8a15 15 0 0 0 6.6 6.6l2.2-2.2a1 1 0 0 1 1-.25 11.4 11.4 0 0 0 3.6.57 1 1 0 0 1 1 1V20a1 1 0 0 1-1 1A17 17 0 0 1 3 4a1 1 0 0 1 1-1h3.5a1 1 0 0 1 1 1c0 1.25.2 2.45.57 3.57a1 1 0 0 1-.25 1z"/></svg>0120-354-926</p>
    <p class="tel-sub">（06-6912-4537）※電話受付は平日9時〜17時のみ</p>
    <p class="office"><b>そらいるか事務局</b>〒541-0093<br>大阪市中央区東浜町3-2-5-208</p>
  </footer>
</main>
</body>
</html>
```